Premium Gold Vodka Label Design

English ------------------- We need a label for a Vodka Bottle. Its a sparkling premium vodka with gold inside. The design should look premium. We tried it on our selves but it looks horrible. Therefore we need your help. The current name is lumora K, but we are open for any better suggestion. We attached the selfmade design. The label will be printed on the bottle. We have other design jobs for you (logo, other sorts)! English ------------------------ We need a label for a vodka bottle. This is a premium vodka which is offset with gold. The design should look like this. We have tried so far and failed. That is why we need your support. The name is so far lumora K. If you have better suggestions we would be pleased about other suggestions / ideas. In the appendix the failed design is stored. The label is to be applied by screen printing. In the case of good work follow-up projects are guaranteed (logo, other varieties, etc)!
Updates

Project Deadline Extended
Reason: We need more time for the decision.

Target Market(s)

USA

Colors

Designer to choose colors to be used in the design.

Requirements
Must have
• English ------------------------ The needed text is on our selfmade label that is attached. English ------------------------ The required texts are stored in the attached design.
Nice to have
• English ------------------------ Transparent places are allowed because we want to print the label on the bottom. English ------------------------ As the label is applied by screen printing, transparent areas are also possible.

```html
<!DOCTYPE html>
<html lang="en">
<head>
<meta charset="utf-8">
<title>lumora K – Premium Gold Sparkling Vodka Label</title>
<link href="https://fonts.googleapis.com/css2?family=Josefin+Sans:wght@400;600;700&display=swap" rel="stylesheet">
<style>
  :root {
    --ink: #0a0a0a;
    --ink-soft: #161616;
    --white: #ffffff;
    --gold-light: #f3dc9a;
    --gold: #d4a02c;
    --gold-deep: #9a6a1c;
    --bronze: #6b2e1c;
    --page: #ffffff;
  }
  * { box-sizing: border-box; margin: 0; padding: 0; }
  html, body { width: 904px; height: 1200px; overflow: hidden; background: var(--page); }
  body { font-family: "Josefin Sans", sans-serif; }

  .label {
    position: relative;
    width: 904px;
    height: 1200px;
    border-radius: 44px;
    padding: 16px;
    background: linear-gradient(160deg, var(--gold-light) 0%, var(--gold) 25%, var(--bronze) 55%, var(--gold) 80%, var(--bronze) 100%);
  }
  .label__field {
    position: relative;
    width: 100%;
    height: 100%;
    border-radius: 32px;
    overflow: hidden;
    color: var(--white);
  }
  .label__texture {
    position: absolute;
    inset: 0;
    background: linear-gradient(180deg, var(--ink-soft) 0%, var(--ink) 50%, var(--ink-soft) 100%);
  }

  .spec {
    position: absolute;
    top: 70px;
    font-size: 30px;
    font-weight: 600;
    letter-spacing: 0.5px;
  }
  .spec--abv { left: 55px; }
  .spec--proof { right: 56px; }

  .brand {
    position: absolute;
    left: 50%;
    top: 290px;
    transform: translateX(-50%);
    display: flex;
    align-items: center;
    gap: 20px;
    padding: 30px 34px 20px;
    background: #000;
    font-size: 88px;
    font-weight: 400;
    letter-spacing: 7px;
    line-height: 1;
    white-space: nowrap;
  }
  .brand__mark {
    width: 20px;
    height: 20px;
    background: var(--gold);
    margin-bottom: 10px;
  }

  .karat {
    position: absolute;
    left: 50%;
    top: 540px;
    transform: translateX(-50%);
    padding: 10px 14px 2px;
    background: linear-gradient(90deg, var(--gold-deep), var(--gold-light) 45%, var(--gold-deep));
    color: #000;
    font-size: 50px;
    font-weight: 600;
    letter-spacing: -1px;
    line-height: 1;
  }

  .descriptor {
    position: absolute;
    left: 0;
    right: 0;
    text-align: center;
    line-height: 1;
  }
  .descriptor--premium { top: 676px; font-size: 30px; font-weight: 600; }
  .descriptor--vodka {
    top: 718px;
    font-size: 108px;
    font-weight: 600;
    letter-spacing: 8px;
    background: linear-gradient(90deg, var(--gold-deep), var(--gold-light) 40%, var(--gold) 65%, var(--bronze));
    -webkit-background-clip: text;
    background-clip: text;
    color: transparent;
  }
  .descriptor--distilled { top: 812px; font-size: 40px; font-weight: 700; letter-spacing: 1px; }

  .volume {
    position: absolute;
    left: 0; right: 0;
    top: 1044px;
    text-align: center;
    font-size: 50px;
    font-weight: 600;
    line-height: 1;
    background: linear-gradient(90deg, var(--gold-deep), var(--gold-light) 50%, var(--gold-deep));
    -webkit-background-clip: text;
    background-clip: text;
    color: transparent;
  }
  .origin {
    position: absolute;
    left: 0; right: 0;
    top: 1096px;
    text-align: center;
    font-size: 23px;
    letter-spacing: 4px;
    line-height: 1;
  }
</style>
</head>
<body>
  <div class="label">
    <div class="label__field">
      <div class="label__texture" role="img" aria-label="Fine vertical pinstripe pattern on black"></div>

      <div class="spec spec--abv">40%AL. VOL.</div>
      <div class="spec spec--proof">80PROOF</div>

      <div class="brand"><span class="brand__mark"></span>LUMORA K</div>
      <div class="karat">24KT</div>

      <div class="descriptor descriptor--premium">PREMIUM GOLD SPARKLING</div>
      <div class="descriptor descriptor--vodka">VODKA</div>
      <div class="descriptor descriptor--distilled">DISTILLED 8 FILTERED</div>

      <div class="volume">200ML</div>
      <div class="origin">MADE IN GERMANY</div>
    </div>
  </div>
</body>
</html>
```